依頼概要
第33回白鷺川大星火大会
2018年7月14日(土)午後7時30分開会
関東最大級22800発
三大花火師夢の饗宴 桐原煙火工業・宮田火工製作所・藤屋松井火工店
主催:北浜町観光協会・きたはまみなと祭り実行委員会
後援:北浜町・北浜町議会・七森町・北浜町商工会・七森町商工会・北陸あおば農業協同組合
問い合わせ:北浜町観光協会 TEL0280-81-1319
北浜町で検索的なもの
観覧チケットの購入はチケミナで検索的なもの

若干の構成を再度お願いする場合もあります。また、制作いただきました作品に、場合によりこちらで後援や開催日時等軽微な修正をする場合があります。
http://filevault-sample.jp/photo/3c1a9e07b42d58f6a0e9c2147bd86f03e5a1c9d2
上記URLは添付にあるものと同様の使用する写真です

町長様・観光協会様の方で候補作品から選んでいただきました。

ご参加・ご協力ありがとうございました。

```html
<!DOCTYPE html>
<html lang="ja">
<head>
<meta charset="utf-8">
<title>第33回白鷺川大星火大会</title>
<link href="https://fonts.googleapis.com/css2?family=Yuji+Boku&family=Dela+Gothic+One&family=Noto+Sans+JP:wght@500;900&family=Zen+Old+Mincho:wght@900&display=swap" rel="stylesheet">
<style>
:root{
  --night:#07060d;
  --night-2:#1a1020;
  --gold:#f3d27a;
  --gold-deep:#b8862d;
  --crimson:#c4141c;
  --pink:#ff3d8b;
  --yellow:#ffe34a;
  --white:#ffffff;
  --ink:#222;
}
*{margin:0;padding:0;box-sizing:border-box}
html,body{width:849px;height:1200px;overflow:hidden;background:var(--night)}
.poster{position:relative;width:849px;height:1200px;overflow:hidden;font-family:"Noto Sans JP",sans-serif;color:var(--white)}
.fireworks-photo{position:absolute;inset:0;
  background:
    radial-gradient(ellipse 40% 22% at 70% 30%,rgba(255,210,120,.55),transparent 70%),
    radial-gradient(ellipse 35% 20% at 25% 25%,rgba(255,170,80,.45),transparent 70%),
    radial-gradient(ellipse 50% 25% at 50% 70%,rgba(255,190,90,.5),transparent 70%),
    radial-gradient(ellipse 30% 15% at 15% 65%,rgba(230,120,160,.35),transparent 70%),
    linear-gradient(180deg,var(--night-2),var(--night) 80%)}
.vert{position:absolute;writing-mode:vertical-rl;white-space:nowrap}
.edition{position:absolute;left:623px;top:22px;width:198px;height:64px;background:linear-gradient(180deg,#6a0c10,#2b0506);border:2px solid var(--gold-deep);
  font-family:"Zen Old Mincho",serif;font-weight:900;font-size:50px;line-height:60px;text-align:center;color:var(--gold);letter-spacing:2px}
.title{font-family:"Yuji Boku",serif;color:var(--gold);line-height:1;
  text-shadow:0 0 6px #000,3px 3px 0 #5a3a0a,0 0 18px rgba(0,0,0,.8)}
.title-river{left:665px;top:92px;font-size:150px;letter-spacing:-6px}
.title-event{left:500px;top:180px;font-size:155px;letter-spacing:-8px}
.scale-badge{position:absolute;left:230px;top:92px;width:150px;height:116px;background:var(--crimson);text-align:center;font-family:"Zen Old Mincho",serif;font-weight:900;color:var(--white)}
.scale-badge .big{display:block;font-size:60px;line-height:72px}
.scale-badge .small{display:block;font-size:30px;line-height:36px;color:var(--yellow)}
.shots{left:288px;top:226px;font-family:"Dela Gothic One",sans-serif;font-size:90px;line-height:1;color:var(--pink);text-orientation:upright;letter-spacing:-2px;
  -webkit-text-stroke:3px var(--white);paint-order:stroke fill;text-shadow:0 0 14px rgba(0,0,0,.8)}
.feast{left:128px;top:112px;font-family:"Zen Old Mincho",serif;font-weight:900;font-size:64px;line-height:1;color:var(--white);letter-spacing:-1px;
  text-shadow:3px 3px 0 var(--crimson),0 0 10px #000}
.makers{left:30px;top:104px;font-family:"Zen Old Mincho",serif;font-weight:900;font-size:28px;line-height:1;color:var(--yellow);letter-spacing:1px;text-shadow:2px 2px 0 var(--crimson),0 0 8px #000}
.date{position:absolute;left:28px;top:945px;font-family:"Dela Gothic One",sans-serif;color:var(--white);text-shadow:0 0 8px #000}
.date .year{font-size:38px;line-height:1}
.date .day{display:flex;align-items:center;gap:10px;font-size:108px;line-height:1;letter-spacing:-4px}
.date .weekday{display:inline-block;width:64px;height:64px;border-radius:50%;background:var(--crimson);font-family:"Zen Old Mincho",serif;font-weight:900;font-size:42px;line-height:64px;text-align:center;letter-spacing:0}
.date .time{font-family:"Zen Old Mincho",serif;font-weight:900;font-size:40px;line-height:50px;margin-top:4px}
.date .venue{font-family:"Zen Old Mincho",serif;font-weight:900;font-size:34px;line-height:44px}
.date .venue .place{font-size:28px;margin-right:6px}
.credits{position:absolute;left:440px;top:962px;width:400px;font-size:13px;line-height:20px;font-weight:500;color:var(--white);text-shadow:0 0 4px #000}
.search{position:absolute;top:1052px;height:66px;border:2px solid var(--white);background:rgba(0,0,0,.55);padding:4px 8px;font-size:12px;line-height:16px;font-weight:500}
.search-town{left:440px;width:190px}
.search-ticket{left:638px;width:200px}
.search .field{display:flex;align-items:center;gap:6px;margin-top:6px}
.search .word{flex:1;background:var(--white);color:var(--ink);font-weight:900;font-size:15px;line-height:28px;padding-left:6px}
.search .btn{display:flex;align-items:center;gap:3px;background:var(--crimson);padding:0 6px;height:28px;font-weight:900;font-size:13px}
</style>
</head>
<body>
<main class="poster">
  <div class="fireworks-photo" role="img" aria-label="夜空いっぱいに開く黄金色の打ち上げ花火の写真"></div>

  <div class="edition">第33回</div>
  <h1>
    <span class="vert title title-river">白鷺川</span>
    <span class="vert title title-event">大星火大会</span>
  </h1>

  <div class="scale-badge"><span class="big">関東</span><span class="small">最大級</span></div>
  <div class="vert shots">22800発‼</div>
  <div class="vert feast">三大花火師夢の饗宴‼</div>
  <div class="vert makers">桐原煙火工業×宮田火工製作所×藤屋松井火工店</div>

  <div class="date">
    <div class="year">2018年</div>
    <div class="day">7/14<span class="weekday">土</span></div>
    <div class="time">午後7時30分開会</div>
    <div class="venue"><span class="place">潮見県北浜町</span>白鷺川河川敷</div>
  </div>

  <div class="credits">
    主催：北浜町観光協会・きたはまみなと祭り実行委員会<br>
    後援：北浜町・北浜町議会・七森町・北浜町商工会・<br>
    　　　七森町商工会・北陸あおば農業協同組合<br>
    問い合わせ：北浜町観光協会　TEL 0290-64-7725
  </div>

  <div class="search search-town">
    詳しい情報は
    <div class="field"><span class="word">北浜町</span><span class="btn">
      <svg width="12" height="12" viewBox="0 0 12 12"><circle cx="5" cy="5" r="3.5" fill="none" stroke="#fff" stroke-width="1.6"/><line x1="7.6" y1="7.6" x2="11" y2="11" stroke="#fff" stroke-width="1.8"/></svg>検索</span></div>
  </div>
  <div class="search search-ticket">
    観覧チケットの購入は
    <div class="field"><span class="word">チケミナ</span><span class="btn">
      <svg width="12" height="12" viewBox="0 0 12 12"><circle cx="5" cy="5" r="3.5" fill="none" stroke="#fff" stroke-width="1.6"/><line x1="7.6" y1="7.6" x2="11" y2="11" stroke="#fff" stroke-width="1.8"/></svg>検索</span></div>
  </div>
</main>
</body>
</html>
```